Stationery design for a hip Muslim Travel Agency

We are looking for a colorful and energetic stationery design for a Muslim tour and travel agency. We need a letterhead, A4 folder, business card and loyalty card design.

The designs should be clean and cheerful and have a feeling of a colorful mosaic in a mosque. You can use the Mingleroo avatar and cover photo as the basis.

Pelitaru card is a loyalty card we issue to our clients. This can have a similar feel to the business card and it should NOT have the word "card" added to the logo. Think of airline membership cards.

Target Market(s)

Indonesians, 25-44 years old, Muslim, interesting in Umroh and Haji and other Muslim tours.

Industry/Entity Type

Travel Agent

Contact Information for Business Card

As provided in the .psd file.

Font styles to use
Sans Serif

Colors
27a0d5
33b8a4
00a990
0492cd

Requirements
Must have
• Letterhead design
• A4 folder design
• Business card
• Loyalty card (without the word "card" in the logo)
Nice to have
• Use the mosaic patterns provided in the files. We want to express the theme of colorful Islam.
Should not have
• Don't copy the .psd files provided in the brief. This is just for the content, those files were not prepared by a designer.

```html
<!DOCTYPE html>
<html lang="id">
<head>
<meta charset="utf-8">
<title>Pelitaru – Business Card</title>
<link rel="stylesheet" href="https://fonts.googleapis.com/css2?family=Questrial&display=swap">
<style>
  :root {
    --page-bg: #e9eef2;
    --card-dark: #1e2b10;
    --card-lime: #8fc23a;
    --card-lime-light: #a3d04a;
    --text-dark: #1c2610;
    --logo-text: #f2f4ee;
    --logo-dot: #33b8a4;
  }
  * { box-sizing: border-box; margin: 0; padding: 0; }
  html, body {
    width: 1200px;
    height: 960px;
    overflow: hidden;
    background: var(--page-bg);
    font-family: "Questrial", sans-serif;
  }
  .canvas {
    position: relative;
    width: 1200px;
    height: 960px;
  }
  .business-card {
    position: absolute;
    left: 150px;
    top: 223px;
    width: 900px;
    height: 514px;
    background: var(--card-dark);
    overflow: hidden;
  }
  .brand {
    position: absolute;
    left: 96px;
    top: 196px;
    display: flex;
    align-items: center;
    gap: 16px;
  }
  .brand-dot {
    width: 38px;
    height: 38px;
    border-radius: 50%;
    background: var(--logo-dot);
  }
  .brand-name {
    font-size: 52px;
    color: var(--logo-text);
    letter-spacing: 1px;
  }
  .mosaic-band {
    position: absolute;
    left: 0;
    bottom: 0;
    width: 100%;
    height: 236px;
    background: linear-gradient(135deg, var(--card-lime-light) 0%, var(--card-lime) 100%);
  }
  .band-block {
    position: absolute;
    right: 0;
    top: 278px;
    width: 82px;
    height: 78px;
    background: var(--card-dark);
  }
  .contact {
    position: absolute;
    right: 108px;
    top: 292px;
    text-align: right;
    color: var(--text-dark);
    font-size: 17px;
    line-height: 1.32;
  }
  .contact .person-name { font-size: 22px; }
  .contact .person-name strong { font-weight: 700; font-family: "Questrial", sans-serif; -webkit-text-stroke: 0.6px var(--text-dark); }
  .contact .divider { padding: 0 8px; }
</style>
</head>
<body>
  <main class="canvas">
    <section class="business-card">
      <div class="brand">
        <span class="brand-dot"></span>
        <span class="brand-name">pelitaru.id</span>
      </div>
      <div class="mosaic-band" role="img" aria-label="Lime green band with a soft Islamic mosaic pattern"></div>
      <div class="band-block"></div>
      <div class="contact">
        <p class="person-name"><strong>FIRSTNAME</strong> SECONDNAME</p>
        <p class="designation">DESIGNATION</p>
        <p class="address">Full Address Line</p>
        <p class="web">email@email.com<span class="divider">|</span>www.website.com</p>
        <p class="phone">T.P. 0123456789</p>
      </div>
    </section>
  </main>
</body>
</html>
```